Design Briefpapier
Zielgruppe
Veranstaltungstechnik
Aufgabenstellung
Wir möchten unser Layout (Briefkopf, Header, Footer) neu gestalten lassen. Es existiert bereits ein Logo, das leicht verändert im Header erscheinen soll! WICHTIG: Das Logo soll schwarz hinterlegt werden auf dem Briefpapier, damit das eigentliche Design (orange auf schwarz) auch zur Geltung kommt.
Marke für hochwertige Trauerartikel benötigt Briefpapier Marke für hochwertige Trauerartikel benötigt Briefpapier"
Wir benötigen Briefpapier: Anschreiben, Rechnngsformular in Farbe und in schwarz weiß. Dazu Visitenkarten und ein gleicherscheinenden E-Mail Absender. Das Design sollte so klar wir möglich sein. Der Druck erfolgt auf recyceltem Papier.
Briefpapierbogen-/Visitenkarten-Design für KFZ-Unternehmen Briefpapierbogen-/Visitenkarten-Design für KFZ-Unternehmen"
Wir benötigen ein Briefpapierbogen sowie ein Visitenkarten Design! Folgende Angaben müssen auf dem Briefpapier sein: - Logo (siehe Anhang) - Anschrift (KW Solutions UG (haftungsbeschränkt), Tannweg 7, 75412 Borlingen - Wasserzeichen - GF (Jürgen Talkeni) - Bankverbindung ( IBAN DE42 8157 2290..
Briefpapier für Seehafenspedition im Bereich Zollabfertigung Briefpapier für Seehafenspedition im Bereich Zollabfertigung"
Wir bitten um ein Design für unser Briefpapier. Wir suchen ein hochwertiges Design, das die Werte Vertrauen, Exklusivität und Innovation ausstrahlt. Es soll edel aussehen. Bitte für Telefon, Mail etc. Icons benutzen, damit es für jedermann verständlich ist, unabhängig von der Sprach..
Geschäftspapiere für medizinische Schutzausrüstung Geschäftspapiere für medizinische Schutzausrüstung"
Es sollte clean sein, Farben wie , Weiß, blau, grün, wären von Vorteil. Habe keine besondere Vorstellungen lasse mich gerne überraschen. Siehe .. www.vaskoru.de
Geschäftspapiere für Rechtsanwaltskanzlei Geschäftspapiere für Rechtsanwaltskanzlei"
Bitte inklusive Logo (sollte Recht, Digital/Apps, Medizin illustrieren) - habe das Preisgeld vor diesem Hintergrund erhöht. ------------------------- Die Kanzlei arbeitet an der Schnittstelle von (Medizin-)Recht und Digital. Von daher wären wären Symbole/Gestaltung aus Bereich Medizin, Recht..

```html
<!DOCTYPE html>
<html lang="de">
<head>
<meta charset="utf-8">
<title>brandtkessler – Briefpapier</title>
<link href="https://fonts.googleapis.com/css2?family=Arimo:wght@400;700&display=swap" rel="stylesheet">
<style>
  :root {
    --orange: #ee7d00;
    --ink: #1c1b1f;
    --text: #222222;
    --grey: #9a9a9a;
    --rule: #d4d4d4;
    --paper: #ffffff;
    --backdrop: #ecebe8;
  }
  * { margin: 0; padding: 0; box-sizing: border-box; }
  html, body {
    width: 1200px; height: 1200px; overflow: hidden;
    background: var(--backdrop);
    font-family: "Arimo", Arial, sans-serif;
    color: var(--text);
  }
  .sheet {
    position: absolute; left: 215px; top: 62px;
    width: 770px; height: 1076px;
    background: var(--paper);
    box-shadow: 0 4px 18px rgba(0,0,0,.12);
  }
  .edge-bar { position: absolute; left: 0; width: 9px; }
  .edge-bar--dark { top: 0; height: 365px; background: var(--ink); }
  .edge-bar--orange { top: 365px; bottom: 0; background: var(--orange); }

  .masthead {
    position: absolute; top: 0; right: 0;
    width: 389px; height: 71px;
    background: var(--ink);
    border-bottom-left-radius: 12px;
  }
  .brand-dot {
    position: absolute; left: 26px; top: 18px;
    width: 36px; height: 36px; border-radius: 50%;
    background: var(--orange);
  }
  .brand-name {
    position: absolute; left: 73px; top: 11px;
    font-size: 35px; font-weight: 400; color: #ffffff;
    letter-spacing: -0.3px; line-height: 1;
  }
  .brand-tagline {
    position: absolute; left: 95px; top: 45px;
    font-size: 10px; color: var(--orange);
    letter-spacing: 4.6px; line-height: 1;
  }

  .return-line {
    position: absolute; left: 55px; top: 155px;
    width: 321px; padding-bottom: 3px;
    border-bottom: 1px solid var(--rule);
    font-size: 11px; color: var(--grey); letter-spacing: .3px;
  }
  .sender {
    position: absolute; right: 24px; top: 155px;
    text-align: right; font-size: 10.5px; line-height: 12.5px;
  }
  .sender-tab {
    position: absolute; right: 0; top: 155px;
    width: 6px; height: 38px; background: var(--orange);
  }
  .fold-mark {
    position: absolute; left: 25px; top: 364px;
    width: 23px; height: 2px; background: var(--rule);
  }

  .footer { position: absolute; top: 1032px; left: 0; right: 0; font-size: 5.5px; line-height: 6.8px; }
  .footer-col { position: absolute; top: 0; display: flex; }
  .footer-labels { color: var(--orange); }
  .footer-values { color: var(--text); }
  .footer-divider { position: absolute; top: 0; width: 1px; height: 23px; background: var(--text); }
</style>
</head>
<body>
  <main class="sheet">
    <div class="edge-bar edge-bar--dark"></div>
    <div class="edge-bar edge-bar--orange"></div>

    <header class="masthead">
      <span class="brand-dot"></span>
      <span class="brand-name">brandtkessler</span>
      <span class="brand-tagline">high end audio systeme halvenau</span>
    </header>

    <p class="return-line">brandtkessler GmbH &amp; Co. KGPS Lindauer Str. 1410437 Halvenau</p>

    <address class="sender" style="font-style:normal">
      brandtkessler GmbH &amp; Co. KGPS<br>
      Lindauer Str. 14<br>
      10437 Halvenau
    </address>
    <div class="sender-tab"></div>

    <div class="fold-mark"></div>

    <footer class="footer">
      <div class="footer-col" style="left:140px">
        <div class="footer-labels" style="width:27px">Tel.<br>Fax<br>Email<br>Web</div>
        <div class="footer-values">030 418 227 61<br>030 418 227 62<br>info@brandt-kessler.de<br>www.brandt-kessler.de</div>
      </div>
      <div class="footer-divider" style="left:266px"></div>

      <div class="footer-col" style="left:311px">
        <div class="footer-labels" style="width:28px">Bank<br>BLZ<br>IBAN<br>BIC</div>
        <div class="footer-values">Halvenauer Bank - Konto: 071 28 3300<br>120 40 316<br>DE31 1204 0316 0071 2833 00<br>HALV DE BB 120</div>
      </div>
      <div class="footer-divider" style="left:461px"></div>

      <div class="footer-col" style="left:493px">
        <div class="footer-labels" style="width:57px">USt-ID<br>AG<br>HRA<br>Geschäftsführer</div>
        <div class="footer-values">DE 318 462 905<br>Halvenau Mitte<br>51736 B<br>Tobias Brandt + Lukas Kessler</div>
      </div>
    </footer>
  </main>
</body>
</html>
```